Business Postcard Design for Personal Training Company

Need a postcard design for my company called "Cobalt Stride" Colors are Navy Blue, Blue, Grey and White.

On the front I want there to be pictures and it to feature a box that says "Free Consultation + 50% off your first session!"

And somehow to feature the following phrases " Lose Weight. Gain Muscle."
"Customized Personal training using V-Core, the latest technology in fitness. Reach your fitness goals in just two 25-min sessions per week"

Also want featured the following phrases (maybe on back):

"up to 18 times more effective than a conventional gym workout"

I need the back of the postcard to have all my business information:

Address: 327 Venadero Ave, Building B Suite 518, Costa Mesa CA 92626
Website: cobalt-stride.example
Phone #: (949) 555-0137
E-mail: cobaltstridehealth@mailbox.example

I am going to upload my logo, before and after pictures and pictures of people training on the device. Feel free to use as many/or little photos as you want.

Target Market(s)

Wealthy Adults 40+ years old looking for a personal trainer

Industry/Entity Type

Personal Trainer

Colors
0455a3
85cae6
aaaaaa
ffffff

Requirements
Must have
• At least two of the before and after photos, and two or more photos of people working out on the device.

```html
<!DOCTYPE html>
<html lang="en">
<head>
<meta charset="utf-8">
<title>Cobalt Stride Postcard</title>
<link rel="stylesheet" href="https://fonts.googleapis.com/css2?family=Lato:ital,wght@0,300;0,400;0,700;1,300&display=swap">
<style>
  :root {
    --blue: #2a9bd0;
    --deep-blue: #0a86c0;
    --light-blue: #85cae6;
    --pale-blue: #b9e1f2;
    --ink: #333333;
    --grey: #555555;
    --band: #48484b;
    --white: #ffffff;
  }
  html, body { margin: 0; padding: 0; overflow: hidden; background: var(--white); }
  .postcard {
    position: relative; width: 1200px; height: 930px; overflow: hidden;
    font-family: 'Lato', sans-serif;
    background: radial-gradient(circle at 30% 30%, #ffffff 0%, #f4f4f4 70%, #ececec 100%);
  }
  .wave { position: absolute; left: 0; top: 0; }
  .offer { position: absolute; left: 0; width: 785px; top: 62px; text-align: center;
    color: var(--blue); font-weight: 300; font-size: 43px; line-height: 52px; letter-spacing: 0.5px; margin: 0; }
  .offer strong { font-weight: 700; }
  .headline { position: absolute; left: 0; width: 785px; top: 210px; text-align: center;
    color: var(--ink); font-weight: 300; font-size: 53px; margin: 0; }
  .intro { position: absolute; left: 0; width: 785px; top: 280px; text-align: center;
    color: var(--grey); font-weight: 300; font-size: 25px; line-height: 31px; margin: 0; }
  .goals { position: absolute; left: 0; width: 785px; top: 382px; text-align: center; margin: 0;
    font-size: 35px; line-height: 43px; font-weight: 300; color: var(--ink); }
  .goals .accent { color: var(--blue); display: block; }
  .goals .strong { color: var(--blue); font-weight: 700; display: block; }
  .brand { position: absolute; left: 245px; top: 592px; display: flex; align-items: center; gap: 10px; }
  .brand-mark { width: 34px; height: 34px; border-radius: 50%; background: var(--light-blue); }
  .brand-name { font-size: 30px; font-weight: 700; color: var(--deep-blue); }
  .contact { position: absolute; left: 55px; top: 710px; }
  .contact-label { font-size: 22px; font-weight: 300; color: var(--ink); text-decoration: underline; margin: 0 0 4px 4px; }
  .contact-phone { font-size: 34px; color: var(--blue); margin: 0; font-weight: 400; }
  .contact-email { font-size: 20px; color: var(--grey); margin: 0; font-weight: 400; }
  .social { position: absolute; left: 472px; top: 764px; display: flex; gap: 6px; }
  .social span { width: 38px; height: 38px; border-radius: 50%; background: var(--deep-blue); display: block; }
  .photo { position: absolute; border-radius: 50%; box-sizing: border-box; }
  .photo-training { left: 722px; top: 48px; width: 440px; height: 440px; border: 12px solid rgba(185,225,242,0.85);
    background: linear-gradient(160deg, #e9eef2 0%, #c9d3dc 45%, #3a4f8a 75%, #2c2c34 100%); }
  .photo-before { left: 722px; top: 543px; width: 222px; height: 222px; border: 8px solid var(--light-blue);
    background: linear-gradient(180deg, #eeeeee 0%, #e2d3c5 45%, #222 80%, #ddd 100%); }
  .photo-after { left: 915px; top: 543px; width: 222px; height: 222px; border: 8px solid var(--light-blue);
    background: linear-gradient(180deg, #f2f2f2 0%, #e6d4c4 45%, #222 80%, #e0e0e0 100%); }
  .caption { position: absolute; top: 768px; color: var(--white); font-size: 34px; font-weight: 300; margin: 0; }
  .caption-before { left: 788px; }
  .caption-after { left: 986px; }
  .claim-band { position: absolute; left: 0; top: 828px; width: 1200px; height: 102px; background: var(--band); }
  .claim { position: absolute; left: 0; width: 1200px; top: 16px; text-align: center;
    color: var(--white); font-style: italic; font-weight: 300; font-size: 34px; margin: 0; }
</style>
</head>
<body>
<div class="postcard">
  <svg class="wave" width="1200" height="930" viewBox="0 0 1200 930" aria-hidden="true">
    <defs>
      <linearGradient id="wave-fill" x1="0" y1="0" x2="0" y2="1">
        <stop offset="0" stop-color="#7cc4e5"/>
        <stop offset="0.35" stop-color="#1d91c9"/>
        <stop offset="1" stop-color="#0a86c0"/>
      </linearGradient>
    </defs>
    <path d="M848 0 C 840 150 720 280 700 430 C 685 560 625 690 617 828 L1200 828 L1200 0 Z" fill="url(#wave-fill)"/>
    <path d="M700 828 C 690 700 740 600 800 500 C 880 370 1000 330 1200 320 L1200 360 C 1010 370 900 420 830 520 C 770 610 740 700 745 828 Z" fill="var(--light-blue)" opacity="0.35"/>
  </svg>

  <p class="offer">FREE CONSULTATION <strong>+ 50% OFF</strong><br>YOUR FIRST SESSION!</p>
  <h1 class="headline">Lose Weight. Gain Muscle.</h1>
  <p class="intro">Customized Personal training using V-Core, the latest<br>technology in fitness.</p>
  <p class="goals">REACH YOUR FITNESS GOALS<span class="accent">IN JUST 2</span><span class="strong">25-MIN SESSIONS PER WEEK!</span></p>

  <div class="brand">
    <span class="brand-mark"></span>
    <span class="brand-name">Cobalt Stride</span>
  </div>

  <div class="contact">
    <p class="contact-label">For more information</p>
    <p class="contact-phone">(949) 555-0137</p>
    <p class="contact-email">cobaltstridehealth@mailbox.example</p>
  </div>

  <div class="social" aria-label="Social links"><span></span><span></span><span></span></div>

  <div class="photo photo-training" role="img" aria-label="Photo of a client training on the V-Core device with a trainer"></div>
  <div class="photo photo-before" role="img" aria-label="Before photo of a client"></div>
  <div class="photo photo-after" role="img" aria-label="After photo of a client"></div>
  <p class="caption caption-before">Before</p>
  <p class="caption caption-after">After</p>

  <div class="claim-band">
    <p class="claim">Up to 18 times more effective than a conventional gym workout...</p>
  </div>
</div>
</body>
</html>
```